LanternPips business card for creator of IP TOY (fun) (children) designs

This business card will be the introduction of me as the creator of new designs to the toy industry and beyond. These designs are kept secret until being revealed one on one to each company. My design is patent pending protected IP. I am looking for business appropriate with a tinge of fun. Please no black backgounds as this is the toy industry. Be creative with the logo and colors please. Just imagine.

Target Market(s)

TOY Industry Executives - Inventor Relations - Manufacturers this is my first introduction card.

Industry/Entity Type

Toy Industry - I have included our Brand colors which can be seen on the cover of The Quiet Pebble Moon book so uses for any of these others colors would be intersting.

Contact Information for Business Card

LOGO Mara Delwyn Founder Creator 555 017 2869 4718 E Hollin Bend Corvale, KS 70812 www.lanternpips-demo.com maradelwyn@quillpost-mail.com Patent Pending IP

Font styles to use
Other font styles liked:
• The font used in the logo is Swiss721BT bold I need to see other fonts to be able to decide but need a clean look

Requirements
Must have
• A bit of an artistic flair although the logo is very simple. I am in the toy industry so would like something that sparks the look of being a creator?
Nice to have
• Please try a background other than stark white. Would like to see a play using brand colors?I like the logos which look like they are lifted off the page. Then under the logo the words (not lifted?) Every Play Every Hero Every Lesson
Should not have
• No Black Backgrounds please! should look as clean as possible - I am not opposed to changing to a double sided card if that is more effectual.

```html
<!DOCTYPE html>
<html lang="en">
<head>
<meta charset="utf-8">
<title>LanternPips Business Card</title>
<link href="https://fonts.googleapis.com/css2?family=Poppins:wght@400;500;700;800&display=swap" rel="stylesheet">
<style>
  :root {
    --bg: #dcdddf;
    --yellow: #f3ca24;
    --red: #e3343a;
    --motif: #e8b02c;
    --white: #ffffff;
  }
  * { margin: 0; padding: 0; box-sizing: border-box; }
  html, body { width: 1200px; height: 900px; overflow: hidden; }
  body {
    background: var(--bg);
    font-family: "Poppins", sans-serif;
    position: relative;
  }
  .card {
    position: absolute;
    left: 320px;
    width: 560px;
    height: 320px;
    border-radius: 24px;
    background: var(--yellow);
    overflow: hidden;
  }
  .card--front { top: 100px; }
  .card--back { top: 480px; }
  .card__shapes { position: absolute; inset: 0; width: 100%; height: 100%; }

  .identity { position: absolute; left: 42px; top: 36px; color: var(--red); }
  .identity__name { font-weight: 800; font-size: 32px; line-height: 1.1; letter-spacing: 0.2px; }
  .identity__title { font-weight: 400; font-size: 19px; margin-top: 2px; letter-spacing: 0.6px; }

  .contact {
    position: absolute; right: 196px; top: 186px;
    list-style: none; color: var(--red);
    font-size: 15px; line-height: 24px; text-align: right;
  }
  .contact li { display: flex; justify-content: flex-end; align-items: center; gap: 10px; }
  .contact svg { width: 14px; height: 14px; flex: none; fill: var(--red); }

  .brand-vertical {
    position: absolute; right: 42px; top: 160px;
    transform: translate(50%, -50%) rotate(90deg);
    color: var(--white); font-weight: 700; font-size: 34px;
    white-space: nowrap; letter-spacing: 0.5px;
  }

  .back-brand {
    position: absolute; left: 0; right: 0; top: 112px;
    text-align: center; color: var(--red);
  }
  .back-brand__name {
    font-weight: 700; font-size: 56px; line-height: 1;
    display: inline-block; padding: 10px 8px;
    border-top: 4px solid var(--red); border-bottom: 4px solid var(--red);
  }
  .back-brand__tagline { font-weight: 500; font-size: 17px; margin-top: 10px; letter-spacing: 0.5px; }
</style>
</head>
<body>

  <section class="card card--front" aria-label="Business card front">
    <svg class="card__shapes" viewBox="0 0 560 320" preserveAspectRatio="none">
      <path d="M0 150 C40 150 60 200 45 240 C30 285 80 310 110 320 L0 320 Z" fill="var(--red)"/>
      <path d="M380 0 C420 60 400 110 420 170 C440 230 400 280 430 320 L560 320 L560 0 Z" fill="var(--red)"/>
      <g role="img" aria-label="Faint toy motif pattern: game controller, rocket, star and hot air balloon" fill="var(--motif)" opacity="0.8">
        <rect x="252" y="20" width="36" height="22" rx="10"/>
        <circle cx="88" cy="150" r="16"/>
        <circle cx="200" cy="150" r="10"/>
        <ellipse cx="310" cy="146" rx="18" ry="20"/>
      </g>
    </svg>

    <div class="identity">
      <div class="identity__name">Mara Delwyn</div>
      <div class="identity__title">Founder Creator</div>
    </div>

    <ul class="contact">
      <li>555 017 2869
        <svg viewBox="0 0 24 24"><path d="M6.6 10.8a15.1 15.1 0 0 0 6.6 6.6l2.2-2.2a1 1 0 0 1 1-.25 11.4 11.4 0 0 0 3.6.57 1 1 0 0 1 1 1V20a1 1 0 0 1-1 1A17 17 0 0 1 3 4a1 1 0 0 1 1-1h3.5a1 1 0 0 1 1 1c0 1.25.2 2.45.57 3.57a1 1 0 0 1-.25 1z"/></svg>
      </li>
      <li>maradelwyn@quillpost-mail.com
        <svg viewBox="0 0 24 24"><path d="M2 5h20v14H2z M3 6l9 7 9-7" stroke="var(--yellow)" stroke-width="1.5"/></svg>
      </li>
      <li>www.lanternpips-demo.com
        <svg viewBox="0 0 24 24"><circle cx="12" cy="12" r="10"/><path d="M2 12h20M12 2c3 3 3 17 0 20M12 2c-3 3-3 17 0 20" stroke="var(--yellow)" stroke-width="1.5" fill="none"/></svg>
      </li>
      <li>4718 E Hollin Bend Corvale, KS 70812
        <svg viewBox="0 0 24 24"><path d="M12 2a7 7 0 0 0-7 7c0 5 7 13 7 13s7-8 7-13a7 7 0 0 0-7-7zm0 9.5A2.5 2.5 0 1 1 12 6.5a2.5 2.5 0 0 1 0 5z"/></svg>
      </li>
    </ul>

    <div class="brand-vertical">LanternPips</div>
  </section>

  <section class="card card--back" aria-label="Business card back">
    <svg class="card__shapes" viewBox="0 0 560 320" preserveAspectRatio="none">
      <path d="M0 0 L230 0 C200 30 150 20 100 40 C50 60 30 90 0 110 Z" fill="var(--red)"/>
      <path d="M560 230 C520 250 480 280 420 285 C380 290 360 305 350 320 L560 320 Z" fill="var(--red)"/>
      <g role="img" aria-label="Faint toy motif pattern: balloon, game controller, teddy bear and toy car" fill="var(--motif)" opacity="0.8">
        <ellipse cx="190" cy="60" rx="22" ry="24"/>
        <rect x="430" y="50" width="60" height="34" rx="14"/>
        <circle cx="90" cy="260" r="24"/>
        <ellipse cx="505" cy="175" rx="30" ry="20"/>
      </g>
    </svg>

    <div class="back-brand">
      <div class="back-brand__name">LanternPips</div>
      <div class="back-brand__tagline">Every Play Every Hero Every Lesson</div>
    </div>
  </section>

</body>
</html>
```